Need to have a client log in screen for work orders and estimate requests.
Nice informational landing page.

Stonefield is a full service general contractor servicing apartment complexes;
maintenance of grounds and apartments - remodeling and construction.

Design Specifics: We are pretty open here. Some good examples are
www.oakhavenworks.com , pellarestates.com and www.norvo7building.com

For the site we need:
Homepage - to explain services
Roofing page
Apartment Page
Client Portal - where clients can set up accounts to set up work/estimate request that will be routed to our email

--Will need coding, plan to host site on Wordpress

Target Market(s)

Multi family, Residential and commercial clients

Industry/Entity Type

Construction

Coding

Coded - Design and coding required

Number of Pages Required

3 page

Font styles to use
Serif

Requirements
Must have
• Client portal
Nice to have
• Not sure. please advise

```html
<!DOCTYPE html>
<html lang="en">
<head>
<meta charset="utf-8">
<title>Stonefield Construction</title>
<link href="https://fonts.googleapis.com/css2?family=Roboto:ital,wght@0,400;0,500;0,700;1,400&display=swap" rel="stylesheet">
<style>
:root{
  --red:#e8333f;
  --red-soft:#f98a8c;
  --ink:#1f1f1f;
  --muted:#555b61;
  --light:#f3f4f6;
  --white:#ffffff;
  --rule:#9aa0a6;
}
*{box-sizing:border-box;margin:0;padding:0}
html,body{width:1200px;height:2198px;overflow:hidden}
body{font-family:'Roboto',sans-serif;color:var(--ink);background:var(--white);position:relative}
.brand-gradient{background:linear-gradient(90deg,var(--red) 0%,var(--red-soft) 100%)}

/* hero */
.hero{position:relative;height:543px}
.hero-photo{position:absolute;inset:0;background:
  radial-gradient(ellipse 330px 260px at 700px 330px,rgba(214,160,138,.95) 0%,rgba(196,150,130,.6) 45%,rgba(196,150,130,0) 100%),
  radial-gradient(ellipse 300px 200px at 720px 150px,rgba(236,230,222,.9) 0%,rgba(200,196,190,.5) 50%,rgba(200,196,190,0) 100%),
  radial-gradient(ellipse 360px 380px at 230px 330px,rgba(226,210,170,.85) 0%,rgba(210,196,160,.4) 55%,rgba(210,196,160,0) 100%),
  linear-gradient(180deg,#98a6b8 0%,#b9b6ae 45%,#a9a39a 75%,#8e8883 100%)}
.site-header{position:absolute;left:0;right:0;top:0;height:66px;border-bottom:1px solid rgba(255,255,255,.45)}
.logo{position:absolute;left:55px;top:18px;display:flex;align-items:center;gap:8px;font-weight:700;font-size:22px;color:var(--ink);letter-spacing:.5px}
.logo-mark{width:14px;height:14px;border-radius:50%;background:var(--red)}
.main-nav{position:absolute;top:24px;left:349px}
.main-nav a{color:var(--white);text-decoration:none;font-size:16px;font-weight:500;text-transform:uppercase;position:absolute;white-space:nowrap}
.account-links{position:absolute;top:16px;right:47px;display:flex;gap:8px}
.btn-outline,.btn-solid{height:32px;border-radius:16px;font-size:13px;font-weight:500;display:flex;align-items:center;justify-content:center;padding:0;white-space:nowrap}
.btn-outline{border:1.5px solid var(--white);color:var(--white);width:62px}
.btn-solid{background:var(--white);color:var(--ink);width:122px}

/* welcome */
.welcome{height:110px;text-align:center;color:var(--white);padding-top:5px}
.welcome h1{font-size:22px;font-weight:700;line-height:34px}
.welcome p{font-size:13px;line-height:20px;margin:19px auto 0;width:1110px}

/* section titles */
.section-title{text-align:center;font-size:22px;font-weight:700;line-height:26px}
.section-title span{color:var(--red)}
.dotted-rule{height:0;border-top:1px dashed var(--rule);margin:0 52px}

/* services */
.services{height:329px;background:var(--light);padding-top:18px}
.services .dotted-rule{margin-top:14px}
.service-grid{display:flex;gap:27px;margin:76px 0 0 51px}
.service-card{position:relative;width:254px;height:124px}
.service-photo{position:absolute;left:0;top:0;width:254px;height:124px;border-radius:2px}
.service-icon{position:absolute;left:104px;top:-24px;width:46px;height:46px;border-radius:50%;background:var(--red);border:2px solid var(--white);display:flex;align-items:center;justify-content:center}
.service-label{position:absolute;left:12px;right:12px;top:104px;height:41px;border-radius:3px;color:var(--white);font-size:16px;font-weight:500;display:flex;align-items:center;justify-content:center;white-space:nowrap;box-shadow:0 2px 4px rgba(0,0,0,.15)}

/* projects */
.projects{height:309px;padding-top:17px}
.projects .dotted-rule{margin-top:13px}
.project-strip{display:flex;margin-top:24px;height:228px}
.project-photo{flex:1;height:228px}

/* testimonials */
.testimonials{height:372px;background:var(--light);padding-top:28px;position:relative}
.testimonials .dotted-rule{margin-top:12px}
.quote{position:absolute;width:410px;font-size:13px;line-height:20px}
.quote p{font-style:italic;color:var(--muted)}
.quote cite{display:block;font-style:normal;font-size:13px;font-weight:500;color:var(--ink);margin-top:10px}
.quote.left{left:51px;text-align:right}
.quote.right{left:738px;text-align:left}
.avatar{position:absolute;width:76px;height:76px;border-radius:50%;background:linear-gradient(135deg,#d8d2cb,#8d847c)}
.divider-v{position:absolute;left:599px;top:115px;height:217px;border-left:1px dashed var(--rule)}
.divider-h{position:absolute;left:52px;right:52px;top:222px;border-top:1px dashed var(--rule)}

/* skyline */
.skyline{height:80px;background:var(--light);position:relative}
.skyline::after{content:"";position:absolute;left:0;right:0;bottom:0;height:34px;background:linear-gradient(90deg,var(--red) 0%,var(--red-soft) 100%);opacity:.9}

/* footer */
.site-footer{height:455px;color:var(--white);position:relative}
.footer-col{position:absolute;top:57px;width:253px}
.footer-col h3{font-size:18px;font-weight:700;line-height:22px;margin-bottom:20px}
.footer-col p{font-size:13px;line-height:20px}
.contact-info p{margin-bottom:13px}
.contact-info b{font-weight:700}
.social{display:flex;gap:11px;margin-top:4px}
.social span{width:14px;height:14px;border-radius:50%;background:var(--white)}
.field{position:absolute;background:var(--white);border-radius:2px;font-size:13px;color:#8a8f94;padding:0 12px;display:flex;align-items:center}
.field.area{align-items:flex-start;padding-top:10px}
.send-btn{position:absolute;left:0;top:182px;width:133px;height:32px;background:var(--white);color:var(--ink);font-size:13px;font-weight:500;border-radius:2px;display:flex;align-items:center;justify-content:center;text-transform:uppercase;white-space:nowrap}
.map{width:253px;height:226px;background:linear-gradient(135deg,#e8e4d8 0%,#d9dfd0 45%,#a9c8e8 100%);border:2px solid var(--white)}
.about-team p{margin-bottom:14px}
.footer-rule{position:absolute;left:52px;right:52px;top:384px;border-top:1px solid rgba(255,255,255,.6)}
.copyright{position:absolute;left:0;right:0;top:412px;text-align:center;font-size:12px;font-weight:500}
</style>
</head>
<body>

<section class="hero">
  <div class="hero-photo" role="img" aria-label="Photo of a hand holding a small model house in front of a blurred apartment building"></div>
  <header class="site-header">
    <div class="logo"><span class="logo-mark"></span>Stonefield</div>
    <nav class="main-nav">
      <a href="#" style="left:0">Home</a>
      <a href="#" style="left:83px">About Us</a>
      <a href="#" style="left:196px">Roofing</a>
      <a href="#" style="left:301px">Apartment</a>
      <a href="#" style="left:432px">Contact</a>
    </nav>
    <div class="account-links">
      <span class="btn-outline">Log In</span>
      <span class="btn-solid">Request a Quote</span>
    </div>
  </header>
</section>

<section class="welcome brand-gradient">
  <h1>Welcome to Stonefield Construction</h1>
  <p>Sed ut perspiciatis unde omnis iste natus error sit voluptatem accusantium doloremque laudantium, totam rem aperiam, eaque ipsa quae ab illo inventore veritatis et quasi architecto beatae vitae dicta sunt explicabo.</p>
</section>

<section class="services">
  <h2 class="section-title">Our <span>Services</span></h2>
  <div class="dotted-rule"></div>
  <div class="service-grid">
    <div class="service-card">
      <div class="service-photo" role="img" aria-label="Photo of an empty glass-walled office floor" style="background:linear-gradient(135deg,#5d7484,#b9c8d2)"></div>
      <div class="service-icon"><svg width="22" height="22" viewBox="0 0 22 22" fill="none" stroke="#fff" stroke-width="2"><rect x="3" y="3" width="14" height="6" rx="1"/><path d="M17 6h2v5h-8v3"/><rect x="9" y="14" width="4" height="6" fill="#fff"/></svg></div>
      <div class="service-label brand-gradient">Tenant Improvement</div>
    </div>
    <div class="service-card">
      <div class="service-photo" role="img" aria-label="Photo of cranes erecting a steel warehouse frame" style="background:linear-gradient(180deg,#6f8bb5,#8a8066)"></div>
      <div class="service-icon"><svg width="22" height="22" viewBox="0 0 22 22" fill="none" stroke="#fff" stroke-width="2"><path d="M3 9l8-5 8 5v10H3z"/><path d="M7 19v-7h8v7M7 15h8"/></svg></div>
      <div class="service-label brand-gradient">Warehouse Construction</div>
    </div>
    <div class="service-card">
      <div class="service-photo" role="img" aria-label="Photo of a ladder in a room under renovation" style="background:linear-gradient(135deg,#e9d3b2,#b88a5c)"></div>
      <div class="service-icon"><svg width="22" height="22" viewBox="0 0 22 22" fill="none" stroke="#fff" stroke-width="2.2"><path d="M4 18L14 8M13 4l5 5M5 4l13 14M15 18l3-3"/></svg></div>
      <div class="service-label brand-gradient">Renovations</div>
    </div>
    <div class="service-card">
      <div class="service-photo" role="img" aria-label="Photo of two site workers in hard hats reviewing plans" style="background:linear-gradient(135deg,#4a7bb0,#c89060)"></div>
      <div class="service-icon"><svg width="22" height="22" viewBox="0 0 22 22" fill="#fff"><path d="M6 9a5 5 0 0110 0z"/><rect x="5" y="9" width="12" height="2"/><circle cx="11" cy="13" r="2.5"/><path d="M5 21a6 5 0 0112 0z"/></svg></div>
      <div class="service-label brand-gradient">Project Management</div>
    </div>
  </div>
</section>

<section class="projects">
  <h2 class="section-title">Latest <span>Projects</span></h2>
  <div class="dotted-rule"></div>
  <div class="project-strip">
    <div class="project-photo" role="img" aria-label="Photo of an open office with a meeting table" style="background:linear-gradient(135deg,#d7dbd8,#7f8a84)"></div>
    <div class="project-photo" role="img" aria-label="Photo of a blue-panelled warehouse under a bright sky" style="background:linear-gradient(180deg,#3f6fb4,#9a9ea3)"></div>
    <div class="project-photo" role="img" aria-label="Photo of a living room with a stone stair wall" style="background:linear-gradient(135deg,#6b5f55,#c79b6b)"></div>
    <div class="project-photo" role="img" aria-label="Photo of a modern reception area" style="background:linear-gradient(135deg,#e4e4e2,#6d6460)"></div>
    <div class="project-photo" role="img" aria-label="Photo of a modern commercial building exterior" style="background:linear-gradient(180deg,#2f6cc8,#c7cdd6)"></div>
  </div>
</section>

<section class="testimonials">
  <h2 class="section-title">What <span>People Say</span></h2>
  <div class="dotted-rule"></div>
  <div class="divider-v"></div>
  <div class="divider-h"></div>

  <blockquote class="quote left" style="top:115px">
    <p>Duis aute irure dolor in reprehenderit in voluptate velit esse cillum dolore eu fugiat nulla pariatur. Excepteur sint occaecat cupidatat non proident, sunt in culpa qui officia deserunt mollit.</p>
    <cite>Evan Marsh, Operations Manager</cite>
  </blockquote>
  <div class="avatar" role="img" aria-label="Portrait photo of the client" style="left:491px;top:114px"></div>

  <div class="avatar" role="img" aria-label="Portrait photo of the client" style="left:633px;top:114px"></div>
  <blockquote class="quote right" style="top:115px">
    <p>Provident, similique sunt in culpa qui officia deserunt mollitia animi, id est laborum et dolorum fuga. Et harum quidem rerum facilis est et expedita distinctio. Nam libero tempore, cum soluta nobis.</p>
    <cite>Nora Vale, Creative Designer</cite>
  </blockquote>

  <blockquote class="quote left" style="top:253px">
    <p>Luis aute irure dolor in reprehenderit in piluptate velit esse cillum dolore eu fugiat nulla pariatur. Excepteur sint occaecat cupidatat non proident, sunt in culpa qui officia deserunt mollit.</p>
    <cite>Irene Poole, Manager</cite>
  </blockquote>
  <div class="avatar" role="img" aria-label="Portrait photo of the client" style="left:491px;top:252px"></div>

  <div class="avatar" role="img" aria-label="Portrait photo of the client" style="left:633px;top:252px"></div>
  <blockquote class="quote right" style="top:253px">
    <p>At vero eos et accusamus et iusto odio dignissimos ducimus qui blanditiis praesentium voluptatum deleniti atque corrupti quos dolores et quas molestias excepturi sint occaecati asperiores.</p>
    <cite>Colin Ashby, Developer</cite>
  </blockquote>
</section>

<div class="skyline" role="img" aria-label="Red city skyline silhouette with an airport tower and planes"></div>

<footer class="site-footer brand-gradient">
  <div class="footer-col contact-info" style="left:52px">
    <h3>Contact Us</h3>
    <p>Please feel free to contact us for any issue. Our staff is available to you from 9AM until 5PM on weekdays.</p>
    <p><b>Phone:</b> 555-218-4093</p>
    <p><b>Office:</b> 4170 Larkin Avenue, Brookvale</p>
    <p><b>Email:</b> hello@stonefieldbuild.com</p>
    <div class="social"><span></span><span></span><span></span><span></span><span></span></div>
  </div>

  <div class="footer-col mail-form" style="left:334px">
    <h3>Feel Free to Mail</h3>
    <div style="position:relative">
      <div class="field" style="left:0;top:0;width:116px;height:31px">Name *</div>
      <div class="field" style="left:135px;top:0;width:116px;height:31px">Email *</div>
      <div class="field" style="left:0;top:51px;width:251px;height:31px">Subject</div>
      <div class="field area" style="left:0;top:103px;width:251px;height:64px">Write Your Message Here...</div>
      <div class="send-btn">Send Message</div>
    </div>
  </div>

  <div class="footer-col" style="left:615px">
    <h3>Headquarters</h3>
    <div class="map" role="img" aria-label="Street map showing the headquarters location"></div>
  </div>

  <div class="footer-col about-team" style="left:895px">
    <h3>About Team</h3>
    <p>Enim congue blandit. Lorem ipsum dolor sit amet, consectetur adipiscing elit. Quisque consectetur interdum finibus. Vestibulum ante ipsum primis in faucibus orci. luctus et ultrices posuere.</p>
    <p>Cubilia cras blandit finibus ipsum, id porttitor arcu volutpat a. Integer iaculis erat nec justo malesuada faucibus vel tempus sapien. Vivamus aliquam euismod tristique.</p>
  </div>

  <div class="footer-rule"></div>
  <p class="copyright">Copyright © Stonefield Construction All rights reserved</p>
</footer>

</body>
</html>
```